Large walking and cycling programme needs a vision poster

We need a visually inspiring poster that promotes the Kestrel Pathways Programmes' vision, key priorities and values. The Kestrel Pathways Programme is a large project in Auckland that will deliver more walking and cycling infrastructure to the city. <br/>Elements that need to be included in the poster are:<br/>Vision - Choice connections for our communities<br/>Key priorities - Our story, Smarter procurement, Our resources<br/>Values - Courageous, Communication, Just do it, Own the bigger programme, Openness and collaboration, Flexibility and open to change

```html
<!DOCTYPE html>
<html lang="en">
<head>
<meta charset="utf-8">
<title>Kestrel Pathways – Vision Poster</title>
<link rel="stylesheet" href="https://fonts.googleapis.com/css2?family=Montserrat:wght@800&family=Oswald:wght@400;500&display=swap">
<style>
  :root {
    --backdrop: #5f6f7f;
    --paper: #ffffff;
    --brand-blue: #2b5596;
    --brand-blue-dark: #1f4580;
    --extrusion: #dfe3ea;
    --extrusion-edge: #c9ced8;
    --text-light: #ffffff;
    --sky: #dfe6ea;
    --foliage: #6f8a4e;
    --foliage-deep: #3f5530;
    --pavement: #9a9e9c;
    --pavement-deep: #5e6462;
    --jersey-red: #c8423c;
    --track-pink: #c65a78;
    --track-pink-deep: #9c3f5a;
    --concrete: #a8a49d;
  }
  * { box-sizing: border-box; margin: 0; padding: 0; }
  html, body {
    width: 1200px; height: 899px; overflow: hidden;
    background: var(--backdrop);
  }
  .poster {
    position: absolute; left: 296px; top: 20px;
    width: 608px; height: 860px;
    background: var(--paper);
    overflow: hidden;
    font-family: "Oswald", sans-serif;
    color: var(--text-light);
  }
  .hero-photo {
    position: absolute; left: 0; top: 0; width: 608px; height: 340px;
    background:
      radial-gradient(ellipse 40% 30% at 12% 62%, rgba(200,66,60,0.55), transparent 70%),
      radial-gradient(ellipse 70% 45% at 70% 8%, var(--foliage), transparent 75%),
      linear-gradient(180deg, var(--sky) 0%, var(--foliage) 26%, var(--foliage-deep) 44%, var(--pavement) 62%, var(--pavement-deep) 100%);
  }
  .hero-title {
    position: absolute; left: 22px; top: 108px;
    font-family: "Montserrat", sans-serif; font-weight: 800;
    font-size: 92px; line-height: 0.95; letter-spacing: 0;
    text-transform: uppercase; color: var(--text-light);
    text-shadow: 0 2px 10px rgba(0,0,0,0.25);
  }
  .hero-title span { display: block; }
  .photo-strip {
    position: absolute; left: 10px; top: 300px; width: 588px; height: 190px;
  }
  .strip-photo {
    position: absolute; width: 192px; height: 158px;
    border: 6px solid var(--paper);
  }
  .strip-photo.crowd {
    left: 0; top: 28px;
    background:
      radial-gradient(ellipse 60% 25% at 50% 70%, rgba(200,66,60,0.45), transparent 70%),
      linear-gradient(180deg, var(--sky) 0%, #c7cdd0 38%, var(--concrete) 60%, #7d7a78 100%);
  }
  .strip-photo.track {
    left: 196px; top: 14px;
    background: linear-gradient(180deg, #cfd4d6 0%, #8c8a86 30%, var(--track-pink) 58%, var(--track-pink-deep) 100%);
  }
  .strip-photo.path {
    left: 392px; top: 0;
    background:
      radial-gradient(ellipse 50% 35% at 60% 10%, var(--foliage), transparent 75%),
      linear-gradient(180deg, #8fa06c 0%, #6f7d5a 40%, #9a9890 70%, #6d6a60 100%);
  }
  .statements { position: absolute; left: 26px; top: 520px; }
  .statement {
    position: relative;
    background: var(--brand-blue);
    box-shadow: 8px -8px 0 var(--extrusion), 14px -4px 0 var(--extrusion-edge);
    padding: 8px 16px 9px;
    margin-bottom: 14px;
    text-transform: uppercase;
  }
  .statement .label { font-size: 15px; font-weight: 500; letter-spacing: 0.5px; line-height: 1.2; }
  .statement .content { font-size: 17px; font-weight: 400; letter-spacing: 0.5px; line-height: 1.3; }
  .statement.vision { width: 400px; }
  .statement.priorities { width: 470px; }
  .statement.values { width: 540px; }
  .footer {
    position: absolute; left: 0; top: 772px; width: 608px; height: 88px;
    background: var(--brand-blue-dark);
    display: flex; align-items: center; justify-content: space-between;
    padding: 0 24px;
  }
  .agency-name {
    display: flex; align-items: center; gap: 10px;
    font-size: 18px; font-weight: 500; letter-spacing: 1px; text-transform: uppercase;
  }
  .agency-dot { width: 18px; height: 18px; border-radius: 50%; background: var(--text-light); flex: none; }
  .contact { display: flex; gap: 12px; font-size: 10.5px; line-height: 1.35; }
  .contact .street { text-align: right; }
  .contact .postal { border-left: 1px solid var(--text-light); padding-left: 12px; }
</style>
</head>
<body>
  <main class="poster">
    <div class="hero-photo" role="img" aria-label="Photo of a crowd of people cycling along a tree-lined city street"></div>
    <h1 class="hero-title"><span>Kestrel</span><span>Pathways</span></h1>

    <div class="photo-strip">
      <div class="strip-photo crowd" role="img" aria-label="Photo of many riders on a wide open road during a cycling event"></div>
      <div class="strip-photo track" role="img" aria-label="Photo of children cycling on a pink cycleway beside a city overpass"></div>
      <div class="strip-photo path" role="img" aria-label="Photo of families cycling along a shared path"></div>
    </div>

    <div class="statements">
      <section class="statement vision">
        <p class="label">Vision</p>
        <p class="content">Choice connections for our communities</p>
      </section>
      <section class="statement priorities">
        <p class="label">Key priorities</p>
        <p class="content">Our story, smarter procurement, our resources</p>
      </section>
      <section class="statement values">
        <p class="label">Values</p>
        <p class="content">Courageous · Communication · Just do it · Own the bigger programme · Openness and collaboration · Flexibility and open to change</p>
      </section>
    </div>

    <footer class="footer">
      <div class="agency-name"><span class="agency-dot"></span>Harbourline Transport Agency</div>
      <div class="contact">
        <p class="street">Level 4, Kauri House<br>18 Quay Lane West<br>Auckland<br>+64 9 555 0142</p>
        <p class="postal">Private Bag 100200<br>Auckland City<br>Auckland 1140<br>New Zealand</p>
      </div>
    </footer>
  </main>
</body>
</html>
```